Rosabellas Vintage China Hire

I need a flyer to be distributed at wedding fairs to promote my collection of vintage bone china tea sets.
The china is available to hire as mis matched pieces which is very popular at the moment.
Can also hire out for baby showers, anniversary or charity events for afternoon tea.
I imagine the flyer to be a vintage floral background or border.
The name of the company is "Rosabellas" Unfortunately I do not have a logo, but imagine the typeface to be a little ornate.
Industry/Entity Type
Wedding

```html
<!DOCTYPE html>
<html lang="en">
<head>
<meta charset="utf-8">
<title>Rosabellas Vintage China Hire – Flyer</title>
<link rel="stylesheet" href="https://fonts.googleapis.com/css2?family=Passion+One:wght@700&family=Lato:wght@400;700&family=Teko:wght@500&display=swap">
<style>
  :root {
    --page: #ece8e1;
    --yellow: #efc72a;
    --yellow-deep: #e0a812;
    --wood: #4a3424;
    --paper: #ffffff;
    --ink: #1b140c;
    --ink-brown: #5a3a10;
    --red: #a52a17;
    --black: #0b0b0b;
  }
  * { margin: 0; padding: 0; box-sizing: border-box; }
  html, body { width: 905px; height: 1200px; overflow: hidden; background: var(--page); }
  .canvas { position: relative; width: 905px; height: 1200px; }
  .flyer-shapes { position: absolute; left: 0; top: 0; }
  .title-card {
    position: absolute; left: 200px; top: 82px; width: 530px; height: 128px;
    background: var(--paper); border-radius: 14px 14px 0 0;
    display: flex; align-items: center; justify-content: center;
  }
  .brand-name {
    font-family: "Passion One", "Arial Black", sans-serif; font-weight: 700;
    font-size: 88px; letter-spacing: 2px; color: var(--red); line-height: 1;
  }
  .content-panel {
    position: absolute; left: 75px; top: 312px; width: 768px; height: 508px;
    background: var(--paper);
  }
  .tea-photo {
    position: absolute; left: 92px; top: 320px; width: 301px; height: 492px;
    background: radial-gradient(ellipse at 55% 60%, #e7cdb6 0%, #c59f86 45%, #8c6a55 100%);
  }
  .info-box {
    position: absolute; left: 406px; width: 420px; padding: 28px 20px 0 20px;
    font-family: "Lato", Arial, sans-serif; font-weight: 700; font-size: 22px; line-height: 28px;
    white-space: nowrap;
  }
  .info-box--intro { top: 320px; height: 154px; background: var(--yellow-deep); color: var(--ink); }
  .info-box--events { top: 489px; height: 151px; background: var(--black); color: var(--paper); padding-top: 26px; }
  .info-box--more { top: 655px; height: 153px; background: var(--yellow-deep); color: var(--ink-brown); padding-top: 16px; }
  .headline {
    position: absolute; left: 60px; top: 935px; width: 795px; text-align: center;
    font-family: "Teko", "Arial Narrow", sans-serif; font-weight: 500;
    font-size: 30px; line-height: 35px; color: var(--ink); text-transform: uppercase;
    white-space: nowrap;
  }
  .headline-line { display: block; }
  .footer-note {
    position: absolute; left: 215px; top: 1043px; width: 532px; text-align: center;
    font-family: "Lato", Arial, sans-serif; font-weight: 700; font-size: 14.5px; line-height: 21px;
    color: var(--paper); white-space: nowrap;
  }
</style>
</head>
<body>
<main class="canvas">
  <svg class="flyer-shapes" width="905" height="1200" viewBox="0 0 905 1200" aria-hidden="true">
    <rect x="62" y="60" width="788" height="1065" fill="var(--yellow)"/>
    <polygon fill="var(--wood)" points="62,250 110,242 160,248 200,238 260,244 330,232 380,238 450,230 520,236 560,226 620,234 690,224 740,230 800,220 850,228 850,868 800,862 740,872 690,862 620,870 560,858 500,868 440,860 380,872 320,862 260,874 200,864 140,876 62,868"/>
    <polyline fill="none" stroke="var(--paper)" stroke-width="4" points="62,250 110,242 160,248 200,238 260,244 330,232 380,238 450,230 520,236 560,226 620,234 690,224 740,230 800,220 850,228"/>
    <polyline fill="none" stroke="var(--paper)" stroke-width="4" points="62,868 140,876 200,864 260,874 320,862 380,872 440,860 500,868 560,858 620,870 690,862 740,872 800,862 850,868"/>
    <path fill="var(--black)" d="M62,1076 L215,1072 L215,1048 Q215,1030 235,1030 L728,1030 Q748,1030 748,1048 L748,1078 L850,1074 L850,1125 L62,1125 Z"/>
    <polyline fill="none" stroke="var(--paper)" stroke-width="3" points="62,1074 215,1070"/>
    <polyline fill="none" stroke="var(--paper)" stroke-width="3" points="748,1076 850,1072"/>
    <polygon fill="var(--red)" points="288,974 330,974 330,1000 288,1000 298,987"/>
    <polygon fill="var(--red)" points="585,974 628,974 618,987 628,1000 585,1000"/>
  </svg>

  <header class="title-card">
    <h1 class="brand-name">ROSABELLAS</h1>
  </header>

  <section class="content-panel"></section>
  <div class="tea-photo" role="img" aria-label="Photo of vintage floral bone china teapots, cups and saucers on a lace tablecloth with small flower vases"></div>

  <p class="info-box info-box--intro">Lorem Ipsum is simply dummy<br>text of the printing and typeset-<br>ting industry. Lorem Ipsum has<br>been the industry's standard</p>
  <p class="info-box info-box--events">We also hire out for baby<br>showers,anniversary or charity<br>events for afternoon tea.</p>
  <p class="info-box info-box--more">Lorem Ipsum is simply dummy<br>text of the printing and typeset-<br>ting industry. Lorem Ipsum has<br>been the industry's standard</p>

  <h2 class="headline"><span class="headline-line">The china is available to hire as mis matched pieces which is very</span><span class="headline-line">popular at the moment.</span></h2>

  <p class="footer-note">Lorem Ipsum is simply dummy text of the printing and typeset-<br>ting industry. Lorem Ipsum has been the industry's standard<br>dummy text ever since the 1500s, Lorem Ipsum is simply dummy</p>
</main>
</body>
</html>
```